" Minha empresa presta serviçoes de estética para gordura localizada, celulite, flacidez, rejuvenescimento, botox, preenchimento, redução de Estrias. Será uma marca licenciada para pessoas que queiram meus protocolos de atendimento. "

```html
<!DOCTYPE html>
<html lang="en">
<head>
<meta charset="utf-8">
<title>Marina Valente Letterhead</title>
<link href="https://fonts.googleapis.com/css2?family=Cormorant+Garamond:wght@500;600&family=Open+Sans:ital,wght@0,400;0,600;1,700&display=swap" rel="stylesheet">
<style>
  :root {
    --backdrop: #e9e8e5;
    --paper: #ffffff;
    --ink: #3a3a3a;
    --ink-soft: #8a8a8a;
    --ink-faint: #b4b4b4;
    --gold: #d9a21b;
    --rule: #dcdcdc;
    --band: #1e1e1e;
    --watermark: #f3f3f3;
  }
  * { box-sizing: border-box; margin: 0; padding: 0; }
  html, body { width: 1200px; height: 1200px; overflow: hidden; }
  body {
    background: var(--backdrop);
    font-family: "Open Sans", Arial, sans-serif;
    color: var(--ink);
    position: relative;
  }
  .letterhead {
    position: absolute;
    left: 210px; top: 50px;
    width: 780px; height: 1100px;
    background: var(--paper);
    box-shadow: 0 4px 18px rgba(0,0,0,0.10);
    overflow: hidden;
  }
  .watermark {
    position: absolute;
    left: 200px; top: 330px;
    width: 380px; height: 380px;
    border-radius: 50%;
    background: var(--watermark);
  }
  .brand {
    position: absolute;
    right: 70px; top: 70px;
    display: flex; flex-direction: column; align-items: center;
  }
  .brand-mark {
    width: 34px; height: 34px; border-radius: 50%;
    background: var(--gold);
    margin-bottom: 12px;
  }
  .brand-name {
    font-family: "Cormorant Garamond", Georgia, serif;
    font-weight: 600;
    font-size: 26px;
    letter-spacing: 2px;
    text-transform: uppercase;
    color: var(--ink);
  }
  .brand-tagline {
    font-family: "Cormorant Garamond", Georgia, serif;
    font-weight: 600;
    font-size: 11px;
    letter-spacing: 4px;
    text-transform: uppercase;
    color: var(--ink-faint);
    margin-top: 2px;
  }
  .recipient {
    position: absolute;
    left: 70px; top: 110px;
    font-size: 14px; line-height: 1.45;
    font-style: italic; font-weight: 700;
    color: var(--ink);
  }
  .reference {
    position: absolute;
    right: 70px; top: 250px;
    text-align: right;
    font-size: 11px; line-height: 1.6;
    color: var(--ink-soft);
  }
  .letter-body {
    position: absolute;
    left: 70px; top: 320px;
    width: 640px;
    font-size: 12px; line-height: 1.75;
    color: var(--ink-soft);
  }
  .letter-body p { margin-bottom: 16px; }
  .sign-off {
    position: absolute;
    left: 70px; top: 760px;
    font-size: 12px; color: var(--ink-soft);
  }
  .signature {
    width: 120px; height: 50px;
    margin: 12px 0 6px;
    background: linear-gradient(90deg, #e6e6e6, #f5f5f5);
    border-radius: 4px;
  }
  .signer-name { font-weight: 600; color: var(--ink); }
  .contact-bar {
    position: absolute;
    left: 50px; right: 50px; bottom: 52px;
    border-top: 1px solid var(--rule);
    padding-top: 16px;
    display: flex; justify-content: space-between;
    font-size: 10.5px; color: var(--ink-soft);
  }
  .contact-item { display: flex; align-items: center; gap: 6px; }
  .contact-item svg { width: 12px; height: 12px; flex: none; }
  .base-band {
    position: absolute; left: 0; right: 0; bottom: 0;
    height: 16px; background: var(--band);
  }
</style>
</head>
<body>
  <main class="letterhead">
    <div class="watermark" aria-hidden="true"></div>

    <header class="brand">
      <span class="brand-mark"></span>
      <span class="brand-name">Marina Valente</span>
      <span class="brand-tagline">Aesthetics &amp; Wellness</span>
    </header>

    <address class="recipient">
      To<br>
      Dr. Rafael Moreno<br>
      Chief Executive Officer<br>
      Moreno Studio Group<br>
      2140 Harbor Avenue<br>
      Lisbon, Portugal 1200
    </address>

    <div class="reference">
      Reference: 0014<br>
      12 April 2024
    </div>

    <section class="letter-body">
      <p>Dear Dr. Moreno,</p>
      <p>Thank you for your interest in our licensed aesthetic care protocols. We are pleased to share the programme overview you requested, covering body contouring, cellulite and firmness treatments, together with facial rejuvenation services.</p>
      <p>Each licence includes full clinical training, step by step treatment guides, brand materials and ongoing support from our team, so every partner clinic delivers the same careful standard of results to its clients.</p>
      <p>We would be glad to arrange a visit to our studio and walk you through the next steps. Please let us know a date that suits you.</p>
    </section>

    <div class="sign-off">
      <p>Yours Sincerely,</p>
      <div class="signature" role="img" aria-label="Handwritten signature"></div>
      <p class="signer-name">Marina Valente</p>
      <p>Founder</p>
    </div>

    <footer class="contact-bar">
      <span class="contact-item">
        <svg viewBox="0 0 12 12"><rect x="1" y="2.5" width="10" height="7" fill="none" stroke="var(--gold)" stroke-width="1.2"/><path d="M1 2.5 L6 6.5 L11 2.5" fill="none" stroke="var(--gold)" stroke-width="1.2"/></svg>
        hello@marinavalente.com
      </span>
      <span class="contact-item">
        <svg viewBox="0 0 12 12"><path d="M3 1 L5 3.5 L4 5 Q5 7 7 8 L8.5 7 L11 9 L9.5 11 Q4 10.5 1 3 Z" fill="var(--gold)"/></svg>
        +351 210 555 014
      </span>
      <span class="contact-item">
        <svg viewBox="0 0 12 12"><circle cx="6" cy="6" r="4.8" fill="none" stroke="var(--gold)" stroke-width="1.2"/><path d="M1.2 6 H10.8 M6 1.2 Q3.5 6 6 10.8 M6 1.2 Q8.5 6 6 10.8" fill="none" stroke="var(--gold)" stroke-width="1"/></svg>
        www.marinavalente.com
      </span>
      <span class="contact-item">
        <svg viewBox="0 0 12 12"><path d="M6 11 Q2 6.5 2 4.5 A4 4 0 0 1 10 4.5 Q10 6.5 6 11 Z" fill="var(--gold)"/><circle cx="6" cy="4.5" r="1.4" fill="#fff"/></svg>
        Rua das Flores 88, Lisbon
      </span>
    </footer>

    <div class="base-band" aria-hidden="true"></div>
  </main>
</body>
</html>
```